Web site design for BrixaForm Software (www.brixaformsoftware.example)

Need the design as well as the html for the website. The brief is given in the attached file.
If possible, would like to use pencil sketches instead of images to give a unique look to the site.
Target Market(s)
small Software product companies
Industry/Entity Type
Software
Coding
Coded - Design and coding required
Number of Pages Required
5+ page

```html
<!DOCTYPE html>
<html lang="en">
<head>
<meta charset="utf-8">
<title>BrixaForm Software</title>
<link rel="stylesheet" href="https://fonts.googleapis.com/css2?family=Montserrat:wght@400;500;600;700&family=Open+Sans:ital,wght@0,400;0,600;1,400&display=swap">
<style>
:root{
  --ink:#111;
  --black:#000;
  --white:#fff;
  --muted:#8a8a8a;
  --tint:#f6f8f8;
  --line:#d9dcdc;
  --hero-a:#6d6c68;
  --hero-b:#a8a49c;
  --hero-rust:#b4532a;
}
*{margin:0;padding:0;box-sizing:border-box}
html,body{width:1200px;height:2980px;overflow:hidden;background:var(--white)}
body{font-family:"Open Sans",Arial,sans-serif;color:var(--ink);position:relative}
h2,h3,.nav,.logo,.welcome{font-family:"Montserrat",Arial,sans-serif}

.topbar{position:absolute;top:0;left:0;width:1200px;height:40px;background:var(--black);color:var(--white);font-size:13px}
.topbar .tag{position:absolute;left:92px;top:10px;font-weight:600}
.topbar .links{position:absolute;right:92px;top:10px;font-size:12px}
.topbar .links span{padding:0 4px}

.header{position:absolute;top:40px;left:0;width:1200px;height:76px;background:var(--white)}
.logo{position:absolute;left:92px;top:20px;font-size:26px;font-weight:700;letter-spacing:9px;color:#222}
.logo span{font-weight:400;color:#777}
.nav{position:absolute;right:92px;top:30px;display:flex;gap:17px;font-size:14px;font-weight:500;color:#222;align-items:center}
.nav .active{font-weight:700}

.hero{position:absolute;top:116px;left:0;width:1200px;height:462px;background:linear-gradient(180deg,var(--hero-a) 0%,var(--hero-b) 55%,var(--hero-rust) 85%,#5b6068 100%)}
.welcome{position:absolute;top:250px;left:0;width:1200px;text-align:center;color:var(--white);font-size:64px;font-weight:700;letter-spacing:1px;line-height:1}
.welcome-sub{position:absolute;top:330px;left:0;width:1200px;text-align:center;color:var(--white);font-family:"Montserrat",Arial,sans-serif;font-size:11px;font-weight:700}
.hero-btn{position:absolute;top:362px;left:573px;width:90px;height:28px;background:var(--white);color:#333;font-size:11px;text-align:center;line-height:28px}

.testimonials{position:absolute;top:578px;left:0;width:1200px;height:466px;background:var(--tint)}
.section-title{position:absolute;left:0;width:1200px;text-align:center;font-family:"Montserrat",Arial,sans-serif;font-weight:600;color:#111}
.testimonials .section-title{top:40px;font-size:24px}
.quote-card{position:absolute;width:400px;height:118px}
.quote-photo{position:absolute;left:0;top:0;width:158px;height:116px;background:linear-gradient(135deg,#c9d3d8,#eef1f2 60%,#8d9aa3)}
.quote-name{position:absolute;left:178px;top:0;font-family:"Montserrat",Arial,sans-serif;font-size:16px;font-weight:600;line-height:20px}
.quote-text{position:absolute;left:178px;top:28px;width:210px;font-size:10px;line-height:16px;color:var(--muted)}

.about{position:absolute;top:1044px;left:0;width:1200px;height:476px;background:var(--white)}
.about h2{position:absolute;left:94px;top:66px;font-size:28px;font-weight:600;letter-spacing:1px}
.about .body{position:absolute;left:94px;top:132px;width:1016px;font-size:11.5px;line-height:18px;color:var(--muted)}
.about .epigraph{font-style:italic;color:#222;margin-bottom:6px}
.about p{margin-bottom:10px}

.clients{position:absolute;top:1520px;left:0;width:1200px;height:320px;background:var(--tint)}
.clients .section-title{top:84px;font-size:28px}
.client{position:absolute;top:166px;width:142px;height:76px;border:3px solid var(--line);background:var(--white)}
.client .mark{position:absolute;left:16px;right:16px;top:20px;height:30px;background:var(--white);box-shadow:0 0 0 1px #eee;display:flex;align-items:center;justify-content:center;gap:5px;font-size:10px;font-weight:600;color:#333}
.client .dot{width:8px;height:8px;border-radius:50%;background:#333}

.services{position:absolute;top:1840px;left:0;width:1200px;height:570px;background:var(--white)}
.services .section-title{top:66px;font-size:28px}
.service{position:absolute;width:320px}
.service svg{position:absolute;left:0;top:0}
.service h3{position:absolute;left:42px;top:4px;font-size:15px;font-weight:600;letter-spacing:.3px}
.service p{position:absolute;left:0;top:46px;width:310px;font-size:11px;line-height:20px;color:var(--muted)}
.service .more{position:absolute;left:0;top:124px;font-size:11px;font-weight:600;color:#222}

.background{position:absolute;top:2410px;left:0;width:1200px;height:506px;background:var(--tint)}
.background h2{position:absolute;left:94px;top:58px;font-size:29px;font-weight:600;letter-spacing:1px}
.background .body{position:absolute;left:92px;top:140px;width:1020px;font-size:11.5px;line-height:18px;color:var(--muted)}
.background p{margin-bottom:12px}

.footer{position:absolute;top:2916px;left:0;width:1200px;height:64px;background:var(--black);color:var(--white)}
.footer .copy{position:absolute;left:90px;top:24px;font-size:11px}
.footer .social{position:absolute;right:90px;top:20px;display:flex;gap:8px}
.footer .social span{width:26px;height:26px;border:1px solid #888;background:#111}
</style>
</head>
<body>

<div class="topbar">
  <div class="tag">infecting engineering with design</div>
  <div class="links"><span>Partner</span>|<span>Stories</span>|<span>Our Work</span>|<span>Accolades</span>|<span>Giving back</span></div>
</div>

<header class="header">
  <div class="logo">BRIXA<span>FORM</span></div>
  <nav class="nav">
    <span class="active">Home</span><span>Services</span><span>About Us</span><span>Expertise</span><span>Engagement Models</span><span>Aglie</span><span>Blog</span><span>Contact Us</span>
    <svg width="14" height="14" viewBox="0 0 14 14" aria-label="Search"><circle cx="6" cy="6" r="4.5" fill="none" stroke="#222" stroke-width="2"/><line x1="9.5" y1="9.5" x2="13" y2="13" stroke="#222" stroke-width="2"/></svg>
  </nav>
</header>

<section class="hero" role="img" aria-label="Harbour scene with dock cranes, storage tanks, ore heaps and wind turbines under a grey sky"></section>
<div class="welcome">WELCOME</div>
<div class="welcome-sub">TO THE BRIXAFORM</div>
<div class="hero-btn">Services</div>

<section class="testimonials">
  <h2 class="section-title">Testimonials</h2>
  <div class="quote-card" style="left:198px;top:118px">
    <div class="quote-photo" role="img" aria-label="Portrait photo of a scientist in a lab coat"></div>
    <div class="quote-name">Odile Varenne</div>
    <div class="quote-text">Perfection is achieved not when there is nothing more to add, but when there is nothing left to take away.</div>
  </div>
  <div class="quote-card" style="left:604px;top:118px">
    <div class="quote-photo" role="img" aria-label="Portrait photo of a man in a suit"></div>
    <div class="quote-name">Teodor Kallis</div>
    <div class="quote-text">We are what we repeatedly do. Excellence, then, is not an act, but a habit</div>
  </div>
  <div class="quote-card" style="left:198px;top:288px">
    <div class="quote-photo" role="img" aria-label="Portrait photo of a scientist in a lab coat"></div>
    <div class="quote-name">Marek Halden</div>
    <div class="quote-text">Look deep into nature, and you will understand everything better</div>
  </div>
  <div class="quote-card" style="left:604px;top:288px">
    <div class="quote-photo" role="img" aria-label="Portrait photo of a scientist in a lab coat"></div>
    <div class="quote-name">Marek Halden</div>
    <div class="quote-text">Look deep into nature, and you will understand everything better</div>
  </div>
</section>

<section class="about">
  <h2>BRIXAFORM</h2>
  <div class="body">
    <div class="epigraph">Though human ingenuity may make various inventions...it will never devise any inventions more beautiful, nor more simple, nor more to the purpose than Nature does; because in her inventions nothing is wanting, and nothing is superfluous...<br>~ Lorenzo Vaccaro, The Vaccaro Notebooks, Vol. II, XIV: Anatomy, Zoology and Physiology</div>
    <p>Design pervades nature. Whether it is the unique symmetry of a snowflake, or the fibonnacci number of a sunflower or nautilus shell, or self replicating fractals, design is everywhere.</p>
    <p>In todays world, Good Design is associated more with tangible products, and User interfaces. But good design has always been part of software engineering. Good design is what enables massive software edifices to remain stable. Good design is UI and UX of course, but it also the process of deciding "what" is required, "how" it is to be built, "who" will build it, and how will its goodness perpetuate itself.</p>
    <p>We are a small but eclectic group of seasoned programmers who infuse rigor and design into solid engineering in software. We love to explore new frontiers in technology – be it Predictive Analytics, Cognitive IOT or AI</p>
    <p>We infuse design into rigorous engineering – not only in software design and UI, but also by using design thinking for deciding what to build; using design for designing the organisational structure of hierarchies, collaborations and communities; for designing the most productive work spaces and processes; and also communities which perpetuate and replicate themselves.</p>
  </div>
</section>

<section class="clients">
  <h2 class="section-title">Our Clients</h2>
  <div class="client" style="left:92px"><div class="mark"><span class="dot"></span>Zentrivo</div></div>
  <div class="client" style="left:268px"><div class="mark"><span class="dot"></span>Halvenrik</div></div>
  <div class="client" style="left:444px"><div class="mark">Pruvella</div></div>
  <div class="client" style="left:620px"><div class="mark"><span class="dot"></span>Ostrimar Labs</div></div>
  <div class="client" style="left:796px"><div class="mark">Quenlory</div></div>
  <div class="client" style="left:972px"><div class="mark">Darvesk</div></div>
</section>

<section class="services">
  <h2 class="section-title">Our Services</h2>

  <div class="service" style="left:94px;top:158px">
    <svg width="22" height="26" viewBox="0 0 22 26"><rect x="3" y="1" width="16" height="24" fill="none" stroke="#888" stroke-width="2"/><rect x="6" y="19" width="10" height="3" fill="#888"/></svg>
    <h3>POC</h3>
    <p>Whether it is a mobile or web app prototype,&amp; or a more complex IOTprototype, our engineers can understand the requirements, the context, the technology stack</p>
    <div class="more">READ MORE</div>
  </div>
  <div class="service" style="left:444px;top:158px">
    <svg width="26" height="24" viewBox="0 0 26 24"><rect x="1" y="6" width="24" height="17" fill="#888"/><rect x="9" y="2" width="8" height="5" fill="none" stroke="#888" stroke-width="2"/></svg>
    <h3>BUILD PRODUCT</h3>
    <p>Our team of analysts, design thinkers and technologists work with client and end users to specify and carve out a product; our technologists architect and design</p>
    <div class="more">READ MORE</div>
  </div>
  <div class="service" style="left:794px;top:158px">
    <svg width="28" height="24" viewBox="0 0 28 24"><path d="M1 23V3h5v9l7-5v5l7-5v5l7-5v16z" fill="#888"/></svg>
    <h3>MAINTAIN PRODUCT</h3>
    <p>We have the ability to quickly understand large, legacy products, write scaffold test cases around them, and then maintain them with minimum team size and</p>
    <div class="more">READ MORE</div>
  </div>

  <div class="service" style="left:94px;top:362px">
    <svg width="26" height="26" viewBox="0 0 26 26"><path d="M13 1l11 5v13l-11 6-11-6V6z" fill="#888"/><path d="M2 6l11 6 11-6M13 12v13" stroke="#fff" stroke-width="1.5" fill="none"/></svg>
    <h3>ODC SETUP</h3>
    <p>We help in setting up Offshore Development centres for small and medium software development companies in Europe and US. More on "Models" section.</p>
    <div class="more">READ MORE</div>
  </div>
  <div class="service" style="left:444px;top:362px">
    <svg width="28" height="22" viewBox="0 0 28 22"><rect x="1" y="3" width="17" height="13" fill="#888"/><path d="M18 8h5l4 4v4h-9z" fill="#888"/><circle cx="7" cy="18" r="3" fill="#888"/><circle cx="22" cy="18" r="3" fill="#888"/></svg>
    <h3>AGILE CONSULTING</h3>
    <p>We help in setting up Offshore Development centres for small and medium software development companies in Europe and US. More on "Models" section.</p>
    <div class="more">READ MORE</div>
  </div>
  <div class="service" style="left:794px;top:362px">
    <svg width="26" height="26" viewBox="0 0 26 26"><circle cx="13" cy="13" r="9" fill="none" stroke="#888" stroke-width="5" stroke-dasharray="4 3"/><circle cx="13" cy="13" r="6" fill="none" stroke="#888" stroke-width="3"/></svg>
    <h3>HIGH END TRAINING</h3>
    <p>We help in setting up Offshore Development centres for small and medium software development companies in Europe and US. More on "Models" section.</p>
    <div class="more">READ MORE</div>
  </div>
</section>

<section class="background">
  <h2>BACKGROUND AND EXPERTISE</h2>
  <div class="body">
    <p>We are primarily server side programmers with expertise in large scale projects – be it Software development tools, Distributed software frameworks, Telecom and mediation software or Business intelligence.</p>
    <p>Over the years, we have been the trusted offshore product development partner for many startups and mid sized software product companies, and have built software products from scratch.</p>
    <p>We have built over 10 software products for startups all over the world. Best in class UI, and APIs have been designed and implemented by us. Often we take a core technology developed in a university, or an idea, and build a product around it.</p>
    <p>We work in cloud, mobile apps, big data and analytics. We are now getting into predictive analytics, machine learning and AI. We have been associated with the leaders of the Agile movement, and have expertise implementing agile practices in BrixaForm as well as other companies.</p>
    <p>We have expertise in Design and architectural interventions – taking a flawed product and breathing life back into it.</p>
    <p>We conduct high end training in Scrum, clean code, and clean design inspired by Uncle Ravi.</p>
    <p>We conduct training in Java, and concurrency.</p>
  </div>
</section>

<footer class="footer">
  <div class="copy">Copyright © 2017 All Right Reserved BRIXAFORM</div>
  <div class="social" aria-label="Social links"><span></span><span></span><span></span><span></span></div>
</footer>

</body>
</html>
```